Graphics Design for Home Page of MORVA Agency Website

+Our Business Profile+
Our company, MORVA Agency, generates income primarily by matching tutors to students. Another avenue of income comes from the advertising in our site. The website is an integral part of our marketing strategy and platform to interface with customers.

*Contest Requirements*
Our purpose is to create an interface for our website that is superior to our competitors. We have provide our home page interface template for our graphics designer to work on.

Contestants are only required to do the graphics design portion of our front page based on our template. Graphics designs are required and not random photos and clip art to be inserted. The winner may be engaged with new terms, to be our graphics designer of the entire site after this contest.

=Design Requirements=
We enjoy the feel and look of the "Minimalism" design approach and we would like to see this approach heavily applied in your designs. Minimalism is a design concept that uses simple, clean and modern icons and graphics. Designers can research these links to explore more from the following sites:
Contestants are recommended to zarvo “minimalism website” for more examples and inspirations.

~Interface Description~
All our functionalities descriptions take reference to the attached pdf file “Home Page”. In the attached file, boxes are used to denote regions to describe our requirements and it does not mean we necessarily want boxes to be planted everywhere.

Blue Zone 1,2 - Contestants are to reference to the plinkerion home page from the top to the region with the rocket section (JPEG file Blue 1-2). This region works in a similar manner but we have added tabs to increase the functionalities. Our company logo (JPEG file Home & Ai Home) will be the home button. Graphics are required in the space of zone 2. Icons may be used for meaningful purposes for the “Teach” and “Learn” buttons in zone 2.

Blue Zone 3 - Contestants are to reference to the “8 icons” region of the plinkerion home page (JPEG file Ad Space). For our home page zone 3 functions like an advertising space to feature some of our tutors.

Red Zone 4 - The 3 spaces will have a very short write up (Provided by us) on each point on “Our Business”, “Our Process” and “Competitive Rates!”. Icons must be designed and place to represent the 3 points meaningfully to catch the users’ attention. Contestants can take reference to JPEG Icon1, JPEG Icon2 and JPEG Icon3.

Green Zone 5 - Tab with the various buttons at the bottom of our home page. Follow button is a button to link up with social sites such as Quillo, Brindlex and Zarvo+.

Orange Zone 6 - “Back to the top” button with an Icon.

@Disclaimer@
We respect the IP of all designers we take reference to and we have no intention to copy or violate their designs. We only use our references to best describe our requirements due to the limitations of communication in this contest. When it is mentioned to take reference to this particular image or site, we are referring to the functions and format. Any contestants found violating the IP of any designers will be reported immediately.

&Grading&
Our grading system is divided into 2 parts: Functional requirements & designs. If your functional requirements are incorrect or missing, 2 stars or lower will be awarded.
Rejected or 1 star - Too many functional requirements are missing/incorrect
2 stars - A few functional requirements are missing/incorrect
3 Stars - All functional requirements are met. Designs need improvement
4 Stars - All functional requirements are met. Designs are somewhere close to what we are seeking
5 Stars - All functional requirements are met. Designs are the one we are seeking

```html
<!DOCTYPE html>
<html lang="en">
<head>
<meta charset="utf-8">
<title>MORVA Agency – Home</title>
<link rel="stylesheet" href="https://fonts.googleapis.com/css2?family=PT+Sans:wght@400;700&family=Roboto:wght@400&display=swap">
<style>
  :root {
    --red: #e4262c;
    --hero-red: #dc2a30;
    --hero-red-dark: #c81f25;
    --page-bg: #efefef;
    --white: #ffffff;
    --text: #4a4a4a;
    --text-soft: #8a8a8a;
    --footer-bg: #d5d5d5;
    --footer-text: #555555;
    --scroll-btn: #d9d9d9;
  }
  * { box-sizing: border-box; margin: 0; padding: 0; }
  html, body { width: 1019px; height: 1200px; overflow: hidden; }
  body {
    position: relative;
    background: var(--page-bg);
    font-family: "PT Sans", Arial, sans-serif;
    color: var(--text);
  }

  /* Header */
  .site-header {
    position: absolute; left: 0; top: 0; width: 1019px; height: 86px;
    background: var(--white);
  }
  .brand {
    position: absolute; left: 164px; top: 30px;
    font-family: "PT Sans", Arial, sans-serif; font-weight: 700;
    font-size: 34px; line-height: 40px; color: #111; letter-spacing: -1px;
    text-decoration: none;
  }
  .main-nav { position: absolute; left: 307px; top: 54px; display: flex; gap: 15px; }
  .main-nav a, .account-nav a {
    font-family: "Roboto", Arial, sans-serif; font-size: 12px; line-height: 14px;
    color: #222; text-decoration: none; text-transform: uppercase;
  }
  .main-nav a.is-active { color: var(--red); }
  .account-nav { position: absolute; left: 770px; top: 48px; display: flex; align-items: center; gap: 16px; }
  .account-nav .btn-signup {
    background: var(--red); color: var(--white);
    height: 27px; padding: 0 8px; display: flex; align-items: center;
  }

  /* Hero */
  .hero {
    position: absolute; left: 0; top: 86px; width: 1019px; height: 298px;
    background: linear-gradient(180deg, var(--hero-red) 0%, var(--hero-red-dark) 100%);
    text-align: center; color: var(--white);
  }
  .hero-title { position: absolute; left: 0; right: 0; top: 48px; font-weight: 400; font-size: 42px; line-height: 50px; }
  .hero-sub { position: absolute; left: 0; right: 0; top: 110px; font-weight: 400; font-size: 32px; line-height: 38px; }
  .hero-btn {
    position: absolute; top: 170px; width: 133px; height: 43px;
    border: 2px solid var(--white); color: var(--white);
    font-size: 21px; line-height: 39px; text-decoration: none;
  }
  .hero-btn--learn { left: 354px; }
  .hero-btn--teach { left: 530px; }

  /* Featured tutors */
  .section-title {
    position: absolute; left: 0; right: 0; top: 400px; text-align: center;
    font-weight: 400; font-size: 23px; line-height: 30px; color: #555;
  }
  .tutor-card {
    position: absolute; width: 164px; height: 210px; background: var(--white);
    box-shadow: 0 1px 4px rgba(0,0,0,0.22);
  }
  .tutor-photo { display: block; width: 164px; height: 164px; }
  .tutor-info { position: relative; padding: 6px 10px 0 11px; }
  .tutor-name { font-size: 19px; line-height: 20px; color: #555; font-weight: 400; }
  .tutor-rate { position: absolute; right: 8px; top: 6px; font-size: 19px; line-height: 20px; color: #555; }
  .tutor-subject { font-size: 11px; line-height: 14px; color: var(--text-soft); }

  /* Features */
  .feature { position: absolute; top: 926px; width: 170px; text-align: center; }
  .feature-icon { display: block; margin: 0 auto; height: 90px; }
  .feature-title { font-weight: 400; font-size: 18px; line-height: 22px; color: #444; margin-top: 14px; }
  .feature-text { font-size: 10px; line-height: 12px; color: #666; margin-top: 3px; }

  /* Back to top */
  .back-to-top {
    position: absolute; left: 873px; top: 1100px; width: 48px; height: 48px;
    border-radius: 50%; background: var(--scroll-btn);
    display: flex; align-items: center; justify-content: center;
  }

  /* Footer */
  .site-footer {
    position: absolute; left: 0; top: 1157px; width: 1019px; height: 43px;
    background: var(--footer-bg);
  }
  .footer-links { position: absolute; left: 151px; top: 14px; display: flex; gap: 14px; }
  .footer-links a { font-size: 10px; line-height: 14px; color: var(--footer-text); text-decoration: none; }
  .social-links { position: absolute; right: 160px; top: 13px; display: flex; gap: 12px; }
  .social-links a { font-size: 12px; line-height: 16px; color: #777; text-decoration: none; }
  .social-links a.is-active { color: var(--red); }
</style>
</head>
<body>

<header class="site-header">
  <a class="brand" href="#">MORVA</a>
  <nav class="main-nav">
    <a class="is-active" href="#">Students</a>
    <a href="#">Tutors</a>
    <a href="#">Charges</a>
    <a href="#">Contact Us</a>
  </nav>
  <nav class="account-nav">
    <a href="#">Login</a>
    <a class="btn-signup" href="#">Sign Up</a>
  </nav>
</header>

<section class="hero" role="img" aria-label="Classroom with desks, tinted red">
  <h1 class="hero-title">Welcome to MORVA</h1>
  <p class="hero-sub">I Want To</p>
  <a class="hero-btn hero-btn--learn" href="#">LEARN</a>
  <a class="hero-btn hero-btn--teach" href="#">TEACH</a>
</section>

<h2 class="section-title">Featured Tutors</h2>

<article class="tutor-card" style="left:201px; top:453px;">
  <div class="tutor-photo" role="img" aria-label="Portrait of a math tutor" style="background:linear-gradient(160deg,#d8d8d8,#9a9a9a);"></div>
  <div class="tutor-info"><h3 class="tutor-name">John Tutor</h3><span class="tutor-rate">$100</span><p class="tutor-subject">Math</p></div>
</article>
<article class="tutor-card" style="left:426px; top:453px;">
  <div class="tutor-photo" role="img" aria-label="Portrait of a history tutor" style="background:linear-gradient(160deg,#efe3d6,#6b4a3e);"></div>
  <div class="tutor-info"><h3 class="tutor-name">Jane Tutor</h3><span class="tutor-rate">$100</span><p class="tutor-subject">History</p></div>
</article>
<article class="tutor-card" style="left:651px; top:453px;">
  <div class="tutor-photo" role="img" aria-label="Portrait of a science tutor" style="background:linear-gradient(160deg,#5d7a45,#c6c2b8);"></div>
  <div class="tutor-info"><h3 class="tutor-name">John Tutor</h3><span class="tutor-rate">$100</span><p class="tutor-subject">Science</p></div>
</article>
<article class="tutor-card" style="left:201px; top:681px;">
  <div class="tutor-photo" role="img" aria-label="Portrait of an English tutor" style="background:linear-gradient(160deg,#8c6446,#2a2220);"></div>
  <div class="tutor-info"><h3 class="tutor-name">Jane Tutor</h3><span class="tutor-rate">$100</span><p class="tutor-subject">English</p></div>
</article>
<article class="tutor-card" style="left:426px; top:681px;">
  <div class="tutor-photo" role="img" aria-label="Portrait of a history tutor" style="background:linear-gradient(160deg,#f2c21d,#2b2b2b);"></div>
  <div class="tutor-info"><h3 class="tutor-name">John Tutor</h3><span class="tutor-rate">$100</span><p class="tutor-subject">History</p></div>
</article>
<article class="tutor-card" style="left:651px; top:681px;">
  <div class="tutor-photo" role="img" aria-label="Portrait of a science tutor" style="background:linear-gradient(160deg,#2f7a52,#1f3a2c);"></div>
  <div class="tutor-info"><h3 class="tutor-name">Jane Tutor</h3><span class="tutor-rate">$100</span><p class="tutor-subject">Science</p></div>
</article>

<section class="feature" style="left:197px;">
  <svg class="feature-icon" width="70" height="90" viewBox="0 0 70 90" fill="none" stroke="#e4262c" stroke-width="4" stroke-linejoin="round" stroke-linecap="round">
    <path d="M22 62 C22 50 8 44 8 28 A27 27 0 0 1 62 28 C62 44 48 50 48 62 Z"/>
    <path d="M25 34 L35 46 L45 34 M35 46 V62"/>
    <rect x="23" y="62" width="24" height="16" rx="2"/>
    <path d="M23 70 H47 M29 84 H41"/>
  </svg>
  <h3 class="feature-title">Our Business</h3>
  <p class="feature-text">Lorem ipsum dolor sit amet, consectetur adipiscing elit. Nam vel turpis a est ullamcorper ullamcorper id et turpis. Duis sit amet scelerisque libero.</p>
</section>

<section class="feature" style="left:423px;">
  <svg class="feature-icon" width="96" height="90" viewBox="0 0 96 96" fill="none" stroke="#e4262c" stroke-width="4" stroke-linejoin="round">
    <path d="M41 4 H55 L57 16 L66 20 L76 13 L86 23 L79 33 L83 42 L94 44 V58 L83 60 L79 69 L86 79 L76 89 L66 82 L57 86 L55 94 H41 L39 86 L30 82 L20 89 L10 79 L17 69 L13 60 L2 58 V44 L13 42 L17 33 L10 23 L20 13 L30 20 L39 16 Z"/>
    <circle cx="48" cy="51" r="14"/>
  </svg>
  <h3 class="feature-title">Our Process</h3>
  <p class="feature-text">Lorem ipsum dolor sit amet, consectetur adipiscing elit. Nam vel turpis a est ullamcorper ullamcorper id et turpis. Duis sit amet scelerisque libero.</p>
</section>

<section class="feature" style="left:649px;">
  <svg class="feature-icon" width="96" height="90" viewBox="0 0 96 90" fill="none" stroke="#e4262c" stroke-width="4">
    <ellipse cx="66" cy="10" rx="26" ry="7"/>
    <path d="M40 10 V62 M92 10 V62 M40 23 A26 7 0 0 0 92 23 M40 36 A26 7 0 0 0 92 36 M40 49 A26 7 0 0 0 92 49 M62 62 A26 7 0 0 0 92 62"/>
    <ellipse cx="30" cy="40" rx="26" ry="7" fill="#efefef"/>
    <path d="M4 40 V80 M56 40 V80 M4 53 A26 7 0 0 0 56 53 M4 66 A26 7 0 0 0 56 66 M4 80 A26 7 0 0 0 56 80"/>
  </svg>
  <h3 class="feature-title">Competitive Rates!</h3>
  <p class="feature-text">Lorem ipsum dolor sit amet, consectetur adipiscing elit. Nam vel turpis a est ullamcorper ullamcorper id et turpis. Duis sit amet scelerisque libero.</p>
</section>

<a class="back-to-top" href="#" aria-label="Back to top">
  <svg width="26" height="16" viewBox="0 0 26 16" fill="none" stroke="#555" stroke-width="2.5" stroke-linecap="round" stroke-linejoin="round"><path d="M2 14 L13 3 L24 14"/></svg>
</a>

<footer class="site-footer">
  <nav class="footer-links">
    <a href="#">About Us</a>
    <a href="#">Terms &amp; Conditions</a>
    <a href="#">Privacy Policy</a>
    <a href="#">Useful information +</a>
  </nav>
  <nav class="social-links">
    <a class="is-active" href="#">Brindlex</a>
    <a href="#">Quillo</a>
    <a href="#">Zarvo+</a>
  </nav>
</footer>

</body>
</html>
```